Make a creative business cards for our agency

We are a creative, digital marketing and IT development agency. We need a new: flat design, modern-corporate, not much elements, two sided business cards based in our logo (which I provide here in jpg and psd).

We prefer a vertical design, please no, qr codes no complex backgrounds, NO TEMPLATES.

We want to include:

Logo/Name of the agency
Slogan
Name
Title
Email
Phone
Web url
Social Media (Facebook, Twitter and Youtube)
You can simulate all this info and just place invented info.

Feel free to propose. Very important is to keep the same dark red color of the logo for a big area in the background of your design, keep the same font type preferably, you can get off of the box I you consider your idea is great.

In the case you need extra material or more brief info, just let me know please.

```html
<!DOCTYPE html>
<html lang="en">
<head>
<meta charset="utf-8">
<title>RV Studio Business Cards</title>
<link href="https://fonts.googleapis.com/css2?family=Open+Sans:wght@400;600&display=swap" rel="stylesheet">
<style>
  :root {
    --brand-red: #7d0a0c;
    --brand-red-light: #951316;
    --ink-black: #1c1c1e;
    --paper-white: #ffffff;
    --muted-white: #d9d9d9;
    --backdrop: #8e9196;
  }
  * { margin: 0; padding: 0; box-sizing: border-box; }
  html, body { width: 1200px; height: 900px; overflow: hidden; }
  body {
    background: var(--backdrop);
    font-family: "Open Sans", sans-serif;
    position: relative;
  }
  .card {
    position: absolute;
    top: 140px;
    width: 380px;
    height: 620px;
    border-radius: 26px;
    overflow: hidden;
    background: var(--brand-red);
  }
  .card--front { left: 170px; }
  .card--back { left: 650px; }

  .brand {
    position: absolute;
    left: 0; right: 0;
    top: 88px;
    display: flex;
    flex-direction: column;
    align-items: center;
    color: var(--paper-white);
  }
  .brand__row { display: flex; align-items: center; gap: 12px; }
  .brand__dot {
    width: 34px; height: 34px; border-radius: 50%;
    background: var(--paper-white);
  }
  .brand__name { font-size: 34px; font-weight: 400; letter-spacing: 0.5px; }
  .brand__slogan { margin-top: 6px; font-size: 12.5px; letter-spacing: 0.3px; }

  .front__shade {
    position: absolute; inset: 0;
    background: var(--ink-black);
    clip-path: polygon(100% 44%, 100% 100%, 10% 100%);
  }
  .social {
    position: absolute;
    display: flex; align-items: center; gap: 8px;
    color: var(--paper-white);
    font-size: 15px;
  }
  .social__dot {
    width: 16px; height: 16px; border-radius: 50%;
    background: var(--paper-white);
  }
  .social--one { left: 34px; bottom: 34px; }
  .social--two { right: 34px; top: 330px; }

  .back__band {
    position: absolute; left: 0; right: 0; top: 0; height: 255px;
    background: var(--brand-red);
    border-bottom: 6px solid var(--brand-red-light);
  }
  .back__lower {
    position: absolute; left: 0; right: 0; top: 255px; bottom: 0;
    background: var(--ink-black);
  }
  .person {
    position: absolute; left: 40px; top: 292px;
    color: var(--paper-white);
  }
  .person__name { font-size: 27px; font-weight: 600; }
  .person__title { font-size: 14px; color: var(--muted-white); margin-top: 2px; }
  .contacts {
    position: absolute; left: 0; top: 392px; right: 0;
    list-style: none;
  }
  .contact {
    display: flex; align-items: center;
    height: 46px; margin-bottom: 10px;
    color: var(--paper-white);
    font-size: 15px;
  }
  .contact__tab {
    width: 74px; height: 38px;
    background: var(--brand-red);
    border-radius: 0 12px 12px 0;
    display: flex; align-items: center; justify-content: flex-end;
    padding-right: 10px;
    margin-right: 16px;
  }
  .contact__icon {
    width: 24px; height: 24px; border-radius: 50%;
    background: var(--paper-white);
    display: flex; align-items: center; justify-content: center;
  }
  .contact__icon svg { width: 14px; height: 14px; }
</style>
</head>
<body>

<section class="card card--front" aria-label="Card front">
  <div class="brand">
    <div class="brand__row"><span class="brand__dot"></span><span class="brand__name">RV Studio</span></div>
    <span class="brand__slogan">Web, Visual, IT &amp; Mkt Solutions</span>
  </div>
  <div class="front__shade"></div>
  <div class="social social--two"><span>rvstudio</span><span class="social__dot"></span></div>
  <div class="social social--one"><span class="social__dot"></span><span>@rvstudio</span></div>
</section>

<section class="card card--back" aria-label="Card back">
  <div class="back__band">
    <div class="brand">
      <div class="brand__row"><span class="brand__dot"></span><span class="brand__name">RV Studio</span></div>
      <span class="brand__slogan">Web, Visual, IT &amp; Mkt Solutions</span>
    </div>
  </div>
  <div class="back__lower"></div>
  <div class="person">
    <div class="person__name">Daniel Reyes</div>
    <div class="person__title">Creative Manager</div>
  </div>
  <ul class="contacts">
    <li class="contact">
      <span class="contact__tab"><span class="contact__icon">
        <svg viewBox="0 0 24 24"><path fill="#7d0a0c" d="M6.6 10.8a15 15 0 0 0 6.6 6.6l2.2-2.2c.3-.3.7-.4 1-.2 1.1.4 2.3.6 3.6.6.6 0 1 .4 1 1V20c0 .6-.4 1-1 1A17 17 0 0 1 3 4c0-.6.4-1 1-1h3.5c.6 0 1 .4 1 1 0 1.3.2 2.5.6 3.6.1.3 0 .7-.2 1z"/></svg>
      </span></span>010-4821-7395
    </li>
    <li class="contact">
      <span class="contact__tab"><span class="contact__icon">
        <svg viewBox="0 0 24 24"><rect x="2" y="5" width="20" height="14" rx="2" fill="#7d0a0c"/><path d="M3 6l9 7 9-7" stroke="#fff" stroke-width="2" fill="none"/></svg>
      </span></span>hello@rvstudio.com
    </li>
    <li class="contact">
      <span class="contact__tab"><span class="contact__icon">
        <svg viewBox="0 0 24 24"><circle cx="12" cy="12" r="9" fill="none" stroke="#7d0a0c" stroke-width="2"/><ellipse cx="12" cy="12" rx="4" ry="9" fill="none" stroke="#7d0a0c" stroke-width="2"/><path d="M3 12h18" stroke="#7d0a0c" stroke-width="2"/></svg>
      </span></span>www.rvstudio.com
    </li>
    <li class="contact">
      <span class="contact__tab"><span class="contact__icon">
        <svg viewBox="0 0 24 24"><circle cx="12" cy="12" r="7" fill="#7d0a0c"/></svg>
      </span></span>your skype address
    </li>
  </ul>
</section>

</body>
</html>
```